Architectural, Engineering and Design Build

Tavonex4.com
Veteran Disabled Certified company is doing business in Architecture, Engineer and Design build - look simialr websites and come up with design follow following website
https://dorsey-kalbin.example/
https://www.velmonteam.example/
https://www.pirnoqa.example/contract-vehicles/service-disabled-veteran-owned-small-business-sdvosb/
https://www.corbelhubnet.example/about/sdvosb/

Target Market(s)

US - Defense and Federal Government

Industry/Entity Type

Colors
0054AA
0677BA
7BADD7
CADEEF
E8F1F8

Requirements
Must have
• Army, American patriotism , Buildings, construction, architecture, engineering
Nice to have
• I need to attract federal government agencies and Defense

```html
<!DOCTYPE html>
<html lang="en">
<head>
<meta charset="utf-8">
<title>Tavonex4 — Architecture, Engineering &amp; Design Build</title>
<link href="https://fonts.googleapis.com/css2?family=Kanit:wght@400;500&family=Lato:wght@400;700&display=swap" rel="stylesheet">
<style>
:root{
  --navy:#1b2467;
  --navy-deep:#232c6f;
  --red:#c9191c;
  --red-bright:#e0161f;
  --ink:#1b1b1f;
  --muted:#555a66;
  --white:#ffffff;
  --sky:#cadeef;
  --pale:#e8f1f8;
}
*{box-sizing:border-box;margin:0;padding:0}
html,body{width:1200px;height:3387px;overflow:hidden}
body{position:relative;font-family:"Lato",sans-serif;color:var(--ink);background:var(--white)}
.abs{position:absolute}
.heading{font-family:"Kanit",sans-serif;font-weight:500}
.btn{position:absolute;display:flex;align-items:center;justify-content:center;border-radius:30px;color:var(--white);font-family:"Kanit",sans-serif;font-weight:500;font-size:20px}
.btn--red{background:var(--red-bright)}
.btn--navy{background:var(--navy)}

/* brand mark */
.brand{position:absolute;display:flex;align-items:center;gap:12px;font-family:"Kanit",sans-serif;font-weight:500;color:var(--navy)}
.brand__dot{border-radius:50%;background:var(--red)}

/* hero */
.hero{left:0;top:0;width:1200px;height:517px;background:linear-gradient(90deg,#f4f5f6 0%,#eef0ef 38%,#9aa48f 55%,#6f7a68 75%,#8b9590 100%)}
.hero__photo{left:520px;top:0;width:680px;height:517px;background:radial-gradient(ellipse at 55% 55%,#8c8f84 0%,#70756b 45%,rgba(150,160,150,0) 80%)}
.hero__fade{left:0;top:0;width:700px;height:517px;background:linear-gradient(90deg,rgba(246,247,247,1) 55%,rgba(246,247,247,0) 100%)}
.nav{left:329px;top:52px;display:flex;gap:40px;font-family:"Kanit",sans-serif;font-size:16px;color:var(--ink)}
.nav a{color:inherit;text-decoration:none}
.nav .is-active{color:var(--navy)}
.hero__call{left:886px;top:34px;font-family:"Kanit",sans-serif;font-size:20px;line-height:28px;color:var(--ink)}
.hero__title{left:105px;top:178px;font-size:42px;line-height:52px;color:var(--ink)}
.hero__text{left:106px;top:293px;width:430px;font-size:16px;line-height:22px;color:var(--muted)}

/* services */
.services{left:0;top:517px;width:1200px;height:687px;background:radial-gradient(circle at 20% 30%,#b81418 0,transparent 40%),radial-gradient(circle at 70% 80%,#d82024 0,transparent 40%),var(--red)}
.section-title--light{color:var(--white);font-size:28px}
.service{position:absolute;left:99px;width:487px;height:119px;border-left:5px solid var(--navy);padding:14px 0 0 20px}
.service--active{background:var(--white)}
.service h3{font-family:"Kanit",sans-serif;font-weight:500;font-size:28px;line-height:36px;color:var(--white)}
.service--active h3{color:var(--ink)}
.service p{margin-top:8px;width:350px;font-size:14px;line-height:22px;color:var(--white)}
.service--active p{color:var(--muted)}
.service__icon{position:absolute;right:10px;top:18px;width:82px;height:82px;border-radius:50%;background:var(--navy);border:2px solid var(--white)}
.services__photo{left:632px;top:658px;width:465px;height:377px;background:linear-gradient(90deg,#b5622f 0%,#8a4a27 35%,#a7d2e6 45%,#a7d2e6 55%,#8a4a27 65%,#b5622f 100%)}

/* about */
.about__mark{left:43px;top:1301px;width:506px;height:407px;display:flex;align-items:center;justify-content:center;gap:20px;font-family:"Kanit",sans-serif;font-weight:500;font-size:78px;color:var(--navy)}
.about__mark span.dot{width:70px;height:70px;border-radius:50%;background:var(--red)}
.about__title{left:601px;top:1334px;font-size:34px;color:var(--ink)}
.about__text{left:601px;top:1396px;width:500px;font-size:14.5px;line-height:25.7px;color:var(--muted)}

/* gallery */
.gallery{left:0;top:1820px;width:1200px;height:661px;background:linear-gradient(180deg,#dfe3ec 0%,#c7cede 60%,#b6bfd2 100%)}
.gallery__title{left:0;top:1880px;width:1200px;text-align:center;font-size:34px;color:var(--ink)}
.tile{position:absolute;width:238px;height:329px;border-radius:119px;border-bottom:4px solid var(--navy);overflow:hidden}
.tile--flags{left:101px;top:1963px;background:linear-gradient(180deg,#c8952c 0%,#8c5a22 50%,#6d7a3a 100%)}
.tile--towers{left:360px;top:2074px;border-top:5px solid var(--red);border-bottom:none;background:linear-gradient(180deg,#3a6fc0 0%,#7fa3cf 55%,#3e4c7c 100%)}
.tile--site{left:611px;top:1978px;background:linear-gradient(180deg,#d7dfe8 0%,#9a7a5c 50%,#6a5e50 100%)}
.tile--model{left:861px;top:2093px;border-top:5px solid var(--navy);border-bottom:none;background:linear-gradient(180deg,#f0f2f4 0%,#c7cbd0 55%,#8e6b55 100%)}
.tile__label{position:absolute;left:0;bottom:40px;width:100%;text-align:center;font-family:"Kanit",sans-serif;font-size:24px;color:var(--white)}

/* contact */
.contact{left:0;top:2481px;width:1200px;height:906px;background:linear-gradient(180deg,#27306f 0%,#222a66 100%)}
.contact__title{left:0;top:2530px;width:1200px;text-align:center;font-size:34px;color:var(--white)}
.field{position:absolute;left:99px;width:496px;height:55px;background:var(--white);border-radius:4px;border-bottom:4px solid var(--navy-deep);padding:14px 10px;font-size:19px;color:#333}
.field--message{height:127px}
.info{position:absolute;left:650px;display:flex;align-items:center;gap:22px;font-family:"Kanit",sans-serif;font-size:18px;color:var(--white)}
.info__icon{width:74px;height:74px;border-radius:50%;border:2px solid var(--white);display:flex;align-items:center;justify-content:center}
.divider{left:101px;top:3100px;width:995px;height:2px;background:#4a5590}
.footer-nav{left:97px;top:3157px;display:flex;gap:40px;font-family:"Kanit",sans-serif;font-size:16px;color:var(--white)}
.socials{left:99px;top:3213px;display:flex;gap:8px}
.socials span{width:52px;height:52px;border-radius:50%;border:2px solid var(--white)}
.copyright{left:98px;top:3298px;font-family:"Kanit",sans-serif;font-size:16px;color:var(--white)}
</style>
</head>
<body>

<section class="hero abs" aria-label="Hero">
  <div class="hero__photo abs" role="img" aria-label="Soldier in camouflage embracing a child wrapped in an American flag"></div>
  <div class="hero__fade abs"></div>
</section>

<div class="brand" style="left:105px;top:48px;font-size:34px">
  <span class="brand__dot" style="width:34px;height:34px"></span>Tavonex4
</div>
<nav class="nav abs">
  <a class="is-active" href="#">Home</a><a href="#">About</a><a href="#">Services</a><a href="#">Project Gallery</a><a href="#">Contact Us</a>
</nav>
<div class="hero__call abs">Call Today To Donate<br>+1 888-888-8888</div>
<h1 class="hero__title heading abs">Planning, Design,<br>Construction &amp; Related</h1>
<p class="hero__text abs">Lorem ipsum dolor sit amet, consectetur adipiscing elit, sed do eiusmod tempor incididunt ut labore et dolore magna aliqua.</p>
<a class="btn btn--red" style="left:104px;top:378px;width:148px;height:50px">Get Started</a>

<section class="services abs" aria-label="Our Services"></section>
<h2 class="section-title--light heading abs" style="left:99px;top:588px">Our Services</h2>

<div class="service service--active" style="top:658px">
  <h3>Architecture</h3>
  <p>Lorem ipsum dolor sit amet, consectetur adipiscing elit, sed do eiusmod</p>
  <span class="service__icon"></span>
</div>
<div class="service" style="top:785px">
  <h3>Engineer</h3>
  <p>Lorem ipsum dolor sit amet, consectetur adipiscing elit, sed do eiusmod</p>
  <span class="service__icon"></span>
</div>
<div class="service" style="top:913px">
  <h3>Design</h3>
  <p>Lorem ipsum dolor sit amet, consectetur adipiscing elit, sed do eiusmod</p>
  <span class="service__icon"></span>
</div>
<div class="services__photo abs" role="img" aria-label="Looking up between two tall brick apartment towers toward the sky"></div>
<a class="btn btn--navy" style="left:526px;top:1088px;width:148px;height:51px">Learn More</a>

<div class="about__mark abs"><span class="dot"></span>Tavonex4</div>
<h2 class="about__title heading abs">About Us</h2>
<p class="about__text abs">Sed ut perspiciatis unde omnis iste natus error sit voluptatem accusantium doloremque laudantium, totam rem aperiam, eaque ipsa quae ab illo inventore veritatis et quasi architecto beatae vitae dicta sunt explicabo. Nemo enim ipsam voluptatem quia voluptas sit aspernatur aut odit aut fugit, sed quia consequuntur magni dolores eos qui ratione voluptatem sequi nesciunt. Neque porro quisquam est, qui dolorem ipsum quia dolor sit amet, consectetur, adipisci velit, sed quia non numquam eius modi tempora incidunt ut labore et dolore magnam aliquam quaerat voluptatem.</p>
<a class="btn btn--red" style="left:600px;top:1662px;width:149px;height:53px">Learn More</a>

<section class="gallery abs" role="img" aria-label="Faded background of a veteran in a wheelchair with a child"></section>
<h2 class="gallery__title heading abs">Project Gallery</h2>
<div class="tile tile--flags" role="img" aria-label="Rows of small American flags along a tree-lined path"></div>
<div class="tile tile--towers" role="img" aria-label="Glass skyscrapers seen from below"><span class="tile__label">Architecture</span></div>
<div class="tile tile--site" role="img" aria-label="Engineers in hard hats reviewing plans on a construction site"></div>
<div class="tile tile--model" role="img" aria-label="Hand holding a building model over technical sketches"></div>

<section class="contact abs" role="img" aria-label="Navy-tinted background of a veteran in a wheelchair holding a flag"></section>
<h2 class="contact__title heading abs">Contact Us</h2>
<div class="field" style="top:2658px">Name</div>
<div class="field" style="top:2720px">Email</div>
<div class="field" style="top:2782px">Subject</div>
<div class="field field--message" style="top:2845px">Message</div>
<a class="btn btn--red" style="left:96px;top:2993px;width:144px;height:50px;font-family:Lato,sans-serif;font-size:17px">Send Now</a>

<div class="info" style="top:2660px">
  <span class="info__icon"><svg width="22" height="30" viewBox="0 0 22 30"><path d="M11 0C5 0 0 5 0 11c0 8 11 19 11 19s11-11 11-19C22 5 17 0 11 0z" fill="#fff"/><circle cx="11" cy="11" r="4" fill="#242d6c"/></svg></span>
  530 modi tempora incidunt ut labore et
</div>
<div class="info" style="top:2769px">
  <span class="info__icon"><svg width="28" height="28" viewBox="0 0 24 24"><path d="M6.6 10.8c1.4 2.8 3.8 5.1 6.6 6.6l2.2-2.2c.3-.3.7-.4 1-.2 1.1.4 2.3.6 3.6.6.6 0 1 .4 1 1V20c0 .6-.4 1-1 1C10.6 21 3 13.4 3 4c0-.6.4-1 1-1h3.5c.6 0 1 .4 1 1 0 1.3.2 2.5.6 3.6.1.3 0 .7-.2 1L6.6 10.8z" fill="#fff"/></svg></span>
  +1 888-888-8888
</div>
<div class="info" style="top:2879px">
  <span class="info__icon"><svg width="32" height="24" viewBox="0 0 32 24"><rect width="32" height="24" rx="3" fill="#fff"/><path d="M2 3l14 11L30 3" stroke="#242d6c" stroke-width="2.5" fill="none"/></svg></span>
  info@tavonex4.com
</div>

<div class="divider abs"></div>
<nav class="footer-nav abs"><span>Home</span><span>About</span><span>Services</span><span>Project Gallery</span><span>Contact Us</span></nav>
<div class="socials abs" aria-label="Social links"><span></span><span></span><span></span><span></span><span></span></div>
<p class="copyright abs">Tavonex4 © 2024 All Right Reserved</p>
<div class="brand" style="left:860px;top:3178px;font-size:44px;color:var(--white)">
  <span class="brand__dot" style="width:34px;height:34px;background:var(--white)"></span>Tavonex4
</div>

</body>
</html>
```